Natural Light/Organic/Documentary Photography Business

I like a simple, approachable, feminine, earthy/organic feel. Earth/neutral tones, nothing too loud or obnoxious. I like the watercolor look. I don't want anything too trendy or something I'll get tired of after a couple months. As far as colors, I am much more a fan of cream/taupe/blue/green...not a fan of pink or purple at all.

Target Market(s)

Weddings & Families

Industry/Entity Type

Wedding Photography

Contact Information for Business Card

website, email, phone number

Font styles to use
Other font styles liked:
• Horizontes, Gotham

Colors

Designer to choose colors to be used in the design.

Requirements
Must have
• Website: www.meliskaverholt.com
• Phone: 482.319.6047
• Email: tessa@meliskaverholt.com
Nice to have
• I like the watercolor look but its not necessary. I like simple/earthy tones. Nothing too loud or distracting. Simple & feminine without being too girly. I like an approachable/soft feel.
• Instagram: www.instagram.com/meliskaverholtphotography/
Should not have
• NO loud colors or design or pattern. I do not want a photo of a camera or lens or anything cheesy like that.

```html
<!DOCTYPE html>
<html lang="en">
<head>
<meta charset="utf-8">
<title>Meliska Verholt Photography – Business Card</title>
<link rel="stylesheet" href="https://fonts.googleapis.com/css2?family=Montserrat:wght@300;400&display=swap">
<style>
  :root {
    --backdrop: #222226;
    --card: #ffffff;
    --taupe: #8c7d71;
    --taupe-soft: #a8998c;
    --icon: #c2ab8e;
    --wash-cream: #f4ecd2;
    --wash-green: #dcebd6;
    --wash-blue: #e2e5f2;
  }
  * { box-sizing: border-box; margin: 0; padding: 0; }
  html, body { width: 1200px; height: 864px; overflow: hidden; }
  body {
    background: var(--backdrop);
    font-family: "Montserrat", sans-serif;
    display: flex;
    align-items: center;
    justify-content: center;
    gap: 80px;
  }
  .card {
    position: relative;
    width: 340px;
    height: 595px;
    background: var(--card);
    border-radius: 26px;
    overflow: hidden;
    box-shadow: 0 18px 40px rgba(0,0,0,.45);
  }
  .artwork-area {
    position: absolute;
    top: 0;
    right: 0;
    width: 190px;
    height: 210px;
    background: linear-gradient(135deg, var(--wash-cream), var(--wash-green) 55%, var(--wash-blue));
  }
  .wordmark {
    position: absolute;
    left: 0;
    right: 0;
    text-align: center;
    color: var(--taupe);
  }
  .wordmark-name {
    font-weight: 300;
    font-size: 27px;
    letter-spacing: 1px;
  }
  .wordmark-tagline {
    margin-top: 8px;
    font-weight: 400;
    font-size: 8.5px;
    letter-spacing: 4px;
    color: var(--taupe-soft);
  }
  .card-front .wordmark { top: 250px; }
  .card-back .wordmark { top: 150px; }
  .contact-list {
    position: absolute;
    left: 32px;
    bottom: 42px;
    list-style: none;
    color: var(--taupe-soft);
    font-size: 12.5px;
    letter-spacing: 1.2px;
  }
  .contact-item {
    display: flex;
    align-items: center;
    gap: 10px;
    margin-top: 8px;
  }
  .contact-icon { width: 13px; height: 13px; flex: none; }
</style>
</head>
<body>
  <section class="card card-front">
    <div class="artwork-area" role="img" aria-label="Watercolour wash artwork in cream, sage green and pale blue"></div>
    <div class="wordmark">
      <p class="wordmark-name">Meliska Verholt</p>
      <p class="wordmark-tagline">PHOTOGRAPHY</p>
    </div>
  </section>

  <section class="card card-back">
    <div class="wordmark">
      <p class="wordmark-name">Meliska Verholt</p>
      <p class="wordmark-tagline">PHOTOGRAPHY</p>
    </div>
    <ul class="contact-list">
      <li class="contact-item">
        <svg class="contact-icon" viewBox="0 0 16 16"><path fill="var(--icon)" d="M4 1l2.5 3-1.5 1.6c.8 1.9 2.4 3.5 4.4 4.4L11 8.5 14 11l-1.6 2.6C7 13.4 2.6 9 2.4 3.6z"/></svg>
        <span>482.319.6047</span>
      </li>
      <li class="contact-item">
        <svg class="contact-icon" viewBox="0 0 16 16"><rect x="1" y="3" width="14" height="10" rx="1" fill="var(--icon)"/><path d="M1.5 3.8L8 9l6.5-5.2" stroke="#fff" stroke-width="1.2" fill="none"/></svg>
        <span>tessa@meliskaverholt.com</span>
      </li>
      <li class="contact-item">
        <svg class="contact-icon" viewBox="0 0 16 16"><circle cx="8" cy="8" r="7" fill="var(--icon)"/><path d="M1 8h14M8 1c-3 3.5-3 10.5 0 14M8 1c3 3.5 3 10.5 0 14" stroke="#fff" stroke-width="1" fill="none"/></svg>
        <span>www.meliskaverholt.com</span>
      </li>
      <li class="contact-item">
        <svg class="contact-icon" viewBox="0 0 16 16"><rect x="1.5" y="1.5" width="13" height="13" fill="none" stroke="var(--icon)" stroke-width="1.4"/></svg>
        <span>meliskaverholtphotography</span>
      </li>
    </ul>
  </section>
</body>
</html>
```